BriskLoom Wordpress Website

We require a WordPress website that emulates the sleek design and functionality of https://www.tulvorix.example and https://quenlap.example/. The site should showcase our AI-powered customer support solutions with a modern, professional aesthetic.
Homepage
The homepage should feature a bold headline highlighting our AI capabilities, followed by concise sections outlining our key offerings:
AI-powered customer support
Data integration and deployment
Knowledge system integration
AI help desks and chat agents
Customer feedback insights
Include eye-catching visuals or animations to illustrate these concepts.
Navigation
The main navigation menu should include:
Product
Platform
Company
News
Learn More
Key Pages
Product Page: Detail our AI solutions, their benefits, and use cases.
Platform Page: Explain our technology, integration capabilities, and deployment process.
Company Page: Share our mission, team, and values.
News Page: Feature latest updates, press releases, and blog posts.
Call-to-Action
Implement a prominent "Learn More" button that directs users to an enrollment page. Our team will manage inquiries from this point.
Footer
Include a "Contact Us" section in the footer for easy access to our contact information.
Design Elements
Use a clean, minimalist design with ample white space
Incorporate a color scheme that reflects trust and innovation
Utilize smooth scrolling and subtle animations for enhanced user experience
Ensure mobile responsiveness for all devices
Technical Requirements
Build on WordPress for easy content management
Optimize for fast loading speeds and SEO
The website should convey our expertise in AI-driven customer support solutions while providing an intuitive user experience that guides visitors toward learning more about our services
Industry/Entity Type
AI Chat Agents

```html
<!DOCTYPE html>
<html lang="en">
<head>
<meta charset="utf-8">
<title>BriskLoom — AI Conversational Platform</title>
<link href="https://fonts.googleapis.com/css2?family=Lexend:wght@300;400;500;600&display=swap" rel="stylesheet">
<style>
:root{
  --ink:#111;
  --body:#2a2a2a;
  --teal-dark:#2c5d61;
  --teal:#3c8a8d;
  --teal-soft:#5fa3a5;
  --mist:#f3f5f5;
  --card:#edf2f2;
  --white:#fff;
  --footer:#2d5c60;
}
*{box-sizing:border-box;margin:0;padding:0}
html,body{width:1200px;height:3506px;overflow:hidden}
body{font-family:"Lexend",sans-serif;color:var(--body);background:var(--white);position:relative}
.abs{position:absolute}
.accent{color:var(--teal)}
.btn{position:absolute;background:var(--teal-dark);color:#fff;font-size:13px;font-weight:500;border-radius:22px;display:flex;align-items:center;justify-content:center;box-shadow:0 6px 14px rgba(44,93,97,.25)}
.fill{position:absolute}

/* header */
.site-header{position:absolute;left:0;top:0;width:1200px;height:70px;background:#fff}
.brand{position:absolute;display:flex;align-items:center;gap:10px;font-weight:400;color:var(--teal-dark);white-space:nowrap}
.brand .dot{border-radius:50%;background:var(--teal-dark);flex:none}
.nav{position:absolute;left:440px;top:27px;display:flex;gap:21px;font-size:13px;color:var(--ink)}

/* hero */
.hero{position:absolute;left:0;top:70px;width:1200px;height:494px;background:var(--mist)}
.eyebrow{left:141px;top:104px;font-size:14px;color:var(--teal-dark)}
.hero h1{position:absolute;left:141px;top:130px;font-size:35px;line-height:47px;font-weight:500;color:var(--ink)}
.hero .lead{left:141px;top:290px;font-size:13.5px;color:var(--ink)}
.badge{position:absolute;top:414px;display:flex;align-items:center;gap:10px;font-size:14px;font-weight:500;color:var(--ink)}

h2.title{position:absolute;font-size:30px;font-weight:500;color:var(--ink);width:1200px;text-align:center;left:0}
.icard{position:absolute;top:732px;width:290px;height:200px;background:var(--card);border-radius:12px;padding:26px 25px}
.icon-round{width:56px;height:56px;border-radius:50%;background:var(--teal-dark);display:flex;align-items:center;justify-content:center;box-shadow:0 6px 12px rgba(44,93,97,.25)}
.icard h3{font-size:17px;font-weight:500;color:var(--ink);margin-top:21px}
.icard p{font-size:12px;line-height:21px;margin-top:9px;color:var(--ink)}

.enable h2{position:absolute;left:501px;top:1062px;font-size:30px;font-weight:500;color:var(--ink)}
.enable p{position:absolute;left:501px;font-size:12px;line-height:23px;color:var(--body)}
.enable h4{position:absolute;left:501px;top:1188px;font-size:15px;font-weight:500;color:var(--ink)}

.features{position:absolute;left:0;top:1443px;width:1200px;height:484px;background:var(--mist)}
.fcard{position:absolute;top:137px;width:213px;height:212px;background:#fff;border-radius:10px;text-align:center;padding:20px 14px}
.fcard h3{font-size:14px;font-weight:500;color:var(--ink);margin-top:14px}
.fcard p{font-size:12.5px;line-height:20px;margin-top:8px;color:#444}
.fcard .arrow{position:absolute;left:50%;bottom:24px;transform:translateX(-50%)}

.trust h2{position:absolute;left:143px;top:2025px;font-size:30px;line-height:41px;font-weight:500;color:var(--ink)}
.checks{position:absolute;left:141px;top:2127px;list-style:none;font-size:14px;color:var(--ink)}
.checks li{display:flex;align-items:center;gap:10px;height:30px}
.trust p{position:absolute;left:141px;top:2224px;font-size:12.5px;line-height:20px;color:var(--ink)}

.why h2{position:absolute;left:604px;top:2478px;font-size:30px;font-weight:500;color:var(--ink)}
.why p{position:absolute;left:604px;top:2536px;width:430px;font-size:12.5px;line-height:22.5px;color:var(--body)}

.footer-band{position:absolute;left:0;top:2985px;width:1200px;height:521px;background:var(--footer)}
.cta{position:absolute;left:141px;top:2840px;width:917px;height:260px;background:var(--card);border-radius:30px;text-align:center}
.cta h2{font-size:30px;font-weight:500;color:var(--ink);margin-top:62px}
.cta p{font-size:12.5px;color:var(--body);margin-top:22px}

.fcol{position:absolute;top:3168px;color:#fff}
.fcol h5{font-size:17px;font-weight:500;margin-bottom:18px}
.fcol ul{list-style:none;font-size:12.5px}
.fcol li{height:27.5px}
.contact li{display:flex;gap:12px;align-items:flex-start;height:auto;margin-bottom:14px;line-height:17px}
.rule{position:absolute;left:141px;top:3450px;width:917px;height:1px;background:rgba(255,255,255,.25)}
.copy{position:absolute;left:141px;top:3470px;font-size:12.5px;color:#fff}
.social{position:absolute;left:926px;top:3466px;display:flex;gap:9px}
.social span{width:26px;height:26px;border-radius:50%;background:#fff;display:block}
</style>
</head>
<body>

<header class="site-header">
  <div class="brand" style="left:141px;top:12px;font-size:30px"><span class="dot" style="width:44px;height:44px"></span>BriskLoom</div>
  <nav class="nav"><span>Home</span><span>Product</span><span>Platform</span><span>Company</span><span>News</span><span>Learn More</span><span>Key Pages</span></nav>
  <div class="btn" style="left:947px;top:14px;width:111px;height:42px">Contact Us</div>
</header>

<section class="hero">
  <div class="abs eyebrow">Meet BriskLoom</div>
  <h1>Elevate Your Users'<br>Experience, A New Type<br>Of <span class="accent">Conversation Awaits</span>.</h1>
  <div class="abs lead">Enhance your customer experience with BriskLoom's AI Assistant.</div>
  <div class="btn" style="left:141px;top:334px;width:114px;height:40px">Get Started</div>
  <div class="badge" style="left:141px"><svg width="24" height="24" viewBox="0 0 24 24"><circle cx="12" cy="12" r="10" fill="none" stroke="#3c8a8d" stroke-width="1.6" stroke-dasharray="4 2"/><path d="M7.5 12.3l3 3 6-6" fill="none" stroke="#3c8a8d" stroke-width="1.8"/></svg>Always Ready</div>
  <div class="badge" style="left:303px"><svg width="30" height="30" viewBox="0 0 30 30"><circle cx="15" cy="15" r="12" fill="none" stroke="#2c5d61" stroke-width="1.6"/><text x="15" y="18" font-size="8" text-anchor="middle" fill="#2c5d61" font-family="Lexend">24/7</text></svg>Always on - 24/7</div>
  <div class="fill" role="img" aria-label="Small chat robot with floating message bubbles" style="left:540px;top:340px;width:190px;height:150px;border-radius:50%;background:radial-gradient(circle,#e4ecf2 0%,rgba(243,245,245,0) 70%)"></div>
  <div class="fill" role="img" aria-label="Smiling young man holding a phone, framed by a teal swirl" style="left:718px;top:48px;width:364px;height:400px;border-radius:50%;background:radial-gradient(circle at 55% 50%,#b9d3e3 0%,#5c9ea0 60%,#2c5d61 100%)"></div>
</section>

<h2 class="title" style="top:650px">Revolutionize Your Customer <span class="accent">Interactions</span></h2>
<div class="icard" style="left:141px"><div class="icon-round"><svg width="28" height="28" viewBox="0 0 28 28" fill="none" stroke="#fff" stroke-width="1.6"><path d="M6 6h12a3 3 0 013 3v6a3 3 0 01-3 3h-6l-4 4v-4H6a3 3 0 01-3-3V9a3 3 0 013-3z"/><path d="M11 10a1.5 1.5 0 113 0c0 1-1.5 1.3-1.5 2.5"/></svg></div><h3>Get Answers</h3><p>Users will find the information they need in seconds</p></div>
<div class="icard" style="left:455px"><div class="icon-round"><svg width="28" height="28" viewBox="0 0 28 28" fill="none" stroke="#fff" stroke-width="1.6"><circle cx="14" cy="11" r="5"/><path d="M12 16v3h4v-3M5 22h18M14 3v2M7 6l1.5 1.5M21 6l-1.5 1.5"/></svg></div><h3>Solve Problems</h3><p>Concerns will be addressed quickly with expert assistance</p></div>
<div class="icard" style="left:769px"><div class="icon-round"><svg width="28" height="28" viewBox="0 0 28 28" fill="none" stroke="#fff" stroke-width="1.6"><path d="M22 6c-6 0-10 4-12 9l3 3c5-2 9-6 9-12z"/><circle cx="17" cy="11" r="1.6"/><path d="M10 15l-4 1 2-4M13 18l-1 4 4-2M8 20l-3 3"/></svg></div><h3>Take Action</h3><p>Users will activate services and features immediately</p></div>

<section class="enable">
  <div class="fill" role="img" aria-label="Man in a denim shirt smiling at his phone, inside a white swirl frame" style="left:142px;top:1023px;width:290px;height:315px;border-radius:50%;background:radial-gradient(circle at 60% 50%,#6e8fa6 0%,#8a7560 55%,#5b4a3a 100%)"></div>
  <h2>BriskLoom <span class="accent">Enables</span> You To</h2>
  <p style="top:1118px">Engage and delight customers with an AI agent aligned to your brand<br>Provide real-time support for a wide variety of uses from simple to complex</p>
  <h4>Make AI Your Own With BriskLoom's Conversational Platform</h4>
  <p style="top:1223px">Ground your BriskLoom AI agent in your company's identity and knowledge<br>Solve problems quickly and effectively</p>
  <div class="fill" role="img" aria-label="Robot character leaning on a smartphone with chat bubbles" style="left:1010px;top:1135px;width:150px;height:240px;border-radius:24px;background:linear-gradient(160deg,#dfe6f5,#2b3a55)"></div>
</section>

<section class="features">
  <h2 class="title" style="top:56px">Key <span class="accent">Features</span></h2>
  <div class="fcard" style="left:141px"><svg width="62" height="46" viewBox="0 0 62 46" fill="none" stroke="#2c5d61" stroke-width="1.6"><rect x="4" y="3" width="54" height="34" rx="2"/><path d="M1 40h60M25 13l-6 7 6 7M37 13l6 7-6 7M33 12l-4 16"/></svg><h3>No-Code Agent Creation</h3><p>Build custom AI agents in minutes using our intuitive interface</p><svg class="arrow" width="22" height="10" viewBox="0 0 22 10" fill="none" stroke="#2c5d61" stroke-width="1.4"><path d="M1 5h19M16 1l4 4-4 4"/></svg></div>
  <div class="fcard" style="left:376px"><svg width="46" height="46" viewBox="0 0 46 46" fill="none" stroke="#2c5d61" stroke-width="1.6"><circle cx="23" cy="20" r="7"/><circle cx="23" cy="20" r="13" stroke-dasharray="5 3"/><path d="M17 38h12M20 42h6M23 33v5"/></svg><h3>Powerful Orchestration</h3><p>Coordinate complex, multi-step workflows across systems</p><svg class="arrow" width="22" height="10" viewBox="0 0 22 10" fill="none" stroke="#2c5d61" stroke-width="1.4"><path d="M1 5h19M16 1l4 4-4 4"/></svg></div>
  <div class="fcard" style="left:611px"><svg width="46" height="46" viewBox="0 0 46 46" fill="none" stroke="#2c5d61" stroke-width="1.6"><path d="M20 8a16 16 0 1016 18H20z"/><path d="M25 3v16h16A16 16 0 0025 3z"/><path d="M28 9l7 7M30 6l8 8"/></svg><h3>Comprehensive Analytics</h3><p>Gain actionable insights from customer interactions</p><svg class="arrow" width="22" height="10" viewBox="0 0 22 10" fill="none" stroke="#2c5d61" stroke-width="1.4"><path d="M1 5h19M16 1l4 4-4 4"/></svg></div>
  <div class="fcard" style="left:845px"><svg width="56" height="46" viewBox="0 0 56 46" fill="none" stroke="#2c5d61" stroke-width="1.6"><path d="M18 16a7 7 0 0113-3 6 6 0 018 6 5 5 0 01-1 10H19a6 6 0 01-1-13z"/><path d="M8 6h8l4 8M48 6h-8l-4 8M8 40h8l4-11M48 40h-8l-4-11M2 23h12M54 23H42"/><circle cx="6" cy="6" r="2"/><circle cx="50" cy="6" r="2"/><circle cx="6" cy="40" r="2"/><circle cx="50" cy="40" r="2"/></svg><h3>Seamless Integration</h3><p>Our platform integrates natively with popular CRM and support tools</p><svg class="arrow" width="22" height="10" viewBox="0 0 22 10" fill="none" stroke="#2c5d61" stroke-width="1.4"><path d="M1 5h19M16 1l4 4-4 4"/></svg></div>
  <div class="btn" style="left:527px;top:392px;width:146px;height:40px">View All Features</div>
</section>

<section class="trust">
  <h2>BriskLoom Prioritizes Trust<br>And <span class="accent">Security</span></h2>
  <ul class="checks">
    <li><svg width="18" height="18" viewBox="0 0 18 18"><circle cx="9" cy="9" r="9" fill="#2c5d61"/><path d="M5 9.3l2.6 2.6L13 6.5" fill="none" stroke="#fff" stroke-width="1.8"/></svg>Built-in supervision and auditing</li>
    <li><svg width="18" height="18" viewBox="0 0 18 18"><circle cx="9" cy="9" r="9" fill="#2c5d61"/><path d="M5 9.3l2.6 2.6L13 6.5" fill="none" stroke="#fff" stroke-width="1.8"/></svg>Secure integrations</li>
    <li><svg width="18" height="18" viewBox="0 0 18 18"><circle cx="9" cy="9" r="9" fill="#2c5d61"/><path d="M5 9.3l2.6 2.6L13 6.5" fill="none" stroke="#fff" stroke-width="1.8"/></svg>Strong data governance and privacy</li>
  </ul>
  <p>Discover how BriskLoom can transform your customer experience<br>with customized conversational AI</p>
  <div class="btn" style="left:141px;top:2287px;width:151px;height:40px">Contact Us Today</div>
  <div class="fill" role="img" aria-label="Smartphone showing a robot chat screen beside a photo of two colleagues at a laptop in a swirl frame" style="left:630px;top:2012px;width:430px;height:328px;border-radius:46% 50% 50% 46%;background:linear-gradient(90deg,#e9edf3 0%,#c8ccd4 40%,#8a6248 75%,#d8cfc6 100%)"></div>
</section>

<section class="why">
  <div class="fill" role="img" aria-label="Waving robot standing on a smartphone with chat bubbles" style="left:160px;top:2420px;width:340px;height:320px;border-radius:40%;background:radial-gradient(circle at 50% 45%,#eef1f4 0%,#c9ced6 45%,rgba(255,255,255,0) 72%)"></div>
  <h2>Why Choose <span class="accent">BriskLoom?</span></h2>
  <p>Transform your customer experience with AI agents that are truly an extension of your brand, created effortlessly through our no-code platform. Request a demo today to see how BriskLoom can revolutionize your support and service operations in record time.</p>
  <div class="btn" style="left:604px;top:2652px;width:111px;height:40px">Learn More</div>
</section>

<div class="footer-band"></div>
<section class="cta">
  <h2>Let's Discuss How We <span class="accent">Can Help You</span></h2>
  <p>Learn how BriskLoom can improve your customer interactions at a lower cost</p>
  <div class="btn" style="left:384px;top:164px;width:150px;height:40px">Contact Us Today</div>
  <div class="fill" role="img" aria-label="Decorative doodle of a paper plane with a dashed flight trail" style="left:600px;top:130px;width:290px;height:110px;border-radius:40px;background:radial-gradient(ellipse,rgba(44,93,97,.08) 0%,rgba(237,242,242,0) 70%)"></div>
</section>

<footer>
  <div class="brand" style="left:141px;top:3280px;font-size:46px;color:#fff;gap:14px"><span class="dot" style="width:72px;height:72px;background:#fff"></span>BriskLoom</div>
  <div class="fcol" style="left:513px"><h5>Quick Links</h5><ul><li>Home</li><li>Product</li><li>Platform</li><li>Company</li><li>News</li><li>Learn More</li><li>Key Pages</li></ul></div>
  <div class="fcol" style="left:692px"><h5>Resources</h5><ul><li>Privacy Policy</li><li>Terms Of Service</li><li>Contact</li></ul></div>
  <div class="fcol contact" style="left:877px"><h5>Contact Info</h5><ul>
    <li><svg width="16" height="18" viewBox="0 0 16 18" fill="none" stroke="#fff" stroke-width="1.6"><path d="M8 17s6-6 6-10A6 6 0 002 7c0 4 6 10 6 10z"/><circle cx="8" cy="7" r="2"/></svg><span>123 Lorem Ipsum Dummy,<br>#567 Dummy Road 1234</span></li>
    <li><svg width="16" height="14" viewBox="0 0 16 14"><rect x="0" y="1" width="16" height="12" rx="1.5" fill="#fff"/><path d="M1 2l7 6 7-6" fill="none" stroke="#2d5c60" stroke-width="1.4"/></svg><span>info@briskloom.example</span></li>
    <li><svg width="16" height="16" viewBox="0 0 16 16"><path d="M3 1l3 3-2 2c1 2 3 4 5 5l2-2 3 3-2 3C7 15 1 9 1 3z" fill="#fff"/></svg><span>123-456-7890</span></li>
  </ul></div>
  <div class="rule"></div>
  <div class="copy">© Copyright 2024 Brisk Loom. All Rights Reserved.</div>
  <div class="social" aria-label="Social links"><span></span><span></span><span></span><span></span></div>
</footer>

</body>
</html>
```